Business Advisory Cards in canvas model

I need a business card to start as an individual advising in business since I am "Bachelor in Business Creation and business innovation" I would like the "Canvas Model" (basic tool to land a business) to represent a part of the logo because it is the simplest and useful model to start, I will advise on business innovation and business creation. Detail: it can be formal, dynamic, colorful, that draws attention, adapted to the millenians.

Target Market(s)

People who want to create their own company. People seeking advice on: negotiation, innovation in business, desing thingking, business creation, coaching in organizational operations, business plan and canvas model.

Contact Information for Business Card

Puede ser colorida pero formal para negociar, que se vea moderna adaptada a los millenians, que se enfoque en “el MAPA DE NEGOCIO”.
Que ocupe toda la tarjeta de ambos lados todo el diseño.

Font styles to use
Sans Serif

Colors

Designer to choose colors to be used in the design.

Requirements
Must have
• Canvas model
Nice to have
• Make it a card that makes the person who receives it want to contact the owner of the card. Make it pleasing to the eye.
Should not have
• Negative images, colors that are lost or damage the eyesight.

```html
<!DOCTYPE html>
<html lang="es">
<head>
<meta charset="utf-8">
<title>Tarjeta de Asesorías Nexo Claro</title>
<link rel="stylesheet" href="https://fonts.googleapis.com/css2?family=Montserrat:wght@500;700;800&display=swap">
<style>
  :root {
    --navy: #1d2b5c;
    --blue: #3b5ca6;
    --ink: #2a2a2e;
    --paper: #ffffff;
    --stage: #eceef2;
  }
  * { box-sizing: border-box; margin: 0; padding: 0; }
  html, body { width: 1200px; height: 1200px; overflow: hidden; }
  body {
    background: var(--stage);
    font-family: "Montserrat", sans-serif;
    display: flex; flex-direction: column; align-items: center; justify-content: center;
    gap: 60px;
  }
  .card {
    width: 840px; height: 480px;
    background: var(--paper);
    box-shadow: 0 8px 24px rgba(20, 30, 60, .18);
    position: relative;
    overflow: hidden;
  }

  /* Front */
  .card-front .contact {
    position: absolute; top: 40px; left: 40px;
    display: flex; align-items: center; gap: 14px;
  }
  .contact-badge {
    width: 58px; height: 58px; border-radius: 12px;
    background: var(--navy);
    display: flex; align-items: center; justify-content: center;
  }
  .contact-name { font-weight: 700; font-size: 17px; color: var(--navy); letter-spacing: .02em; }
  .contact-phone { font-weight: 700; font-size: 20px; color: var(--navy); margin-top: 4px; display: flex; align-items: center; gap: 8px; }
  .brand {
    position: absolute; inset: 0;
    display: flex; flex-direction: column; align-items: center; justify-content: center;
    gap: 14px;
  }
  .brand-row { display: flex; align-items: center; gap: 18px; }
  .brand-dot { width: 64px; height: 64px; border-radius: 50%; background: var(--blue); flex: none; }
  .brand-name { font-weight: 800; font-size: 48px; color: var(--ink); white-space: nowrap; }
  .brand-tagline { font-weight: 500; font-size: 20px; letter-spacing: .5em; color: var(--blue); padding-left: 82px; white-space: nowrap; }
  .card-front .edge-band {
    position: absolute; left: 0; right: 0; bottom: 0; height: 26px;
    background: linear-gradient(90deg, var(--navy), var(--blue));
  }

  /* Back: canvas grid */
  .card-back { padding: 30px; }
  .canvas-grid {
    width: 100%; height: 100%;
    border: 5px solid var(--navy);
    display: grid;
    grid-template-columns: repeat(10, 1fr);
    grid-template-rows: 1fr 1fr 0.9fr;
  }
  .block {
    border: 2.5px solid var(--navy);
    display: flex; align-items: center; justify-content: center;
  }
  .block svg { width: 78px; height: 78px; fill: none; stroke: var(--navy); stroke-width: 5; stroke-linecap: round; stroke-linejoin: round; }
  .partners      { grid-column: 1 / 3;  grid-row: 1 / 3; }
  .activities    { grid-column: 3 / 5;  grid-row: 1 / 2; }
  .resources     { grid-column: 3 / 5;  grid-row: 2 / 3; }
  .value         { grid-column: 5 / 7;  grid-row: 1 / 3; }
  .relationships { grid-column: 7 / 9;  grid-row: 1 / 2; }
  .channels      { grid-column: 7 / 9;  grid-row: 2 / 3; }
  .segments      { grid-column: 9 / 11; grid-row: 1 / 3; }
  .costs         { grid-column: 1 / 6;  grid-row: 3 / 4; }
  .revenue       { grid-column: 6 / 11; grid-row: 3 / 4; }
</style>
</head>
<body>

  <section class="card card-front" aria-label="Frente de la tarjeta">
    <div class="contact">
      <div class="contact-badge">
        <svg width="34" height="34" viewBox="0 0 34 34" fill="#fff" aria-hidden="true">
          <circle cx="17" cy="11" r="7"/>
          <path d="M4 32c0-8 6-12 13-12s13 4 13 12z"/>
        </svg>
      </div>
      <div>
        <p class="contact-name">NOMBRE Y APELLIDO</p>
        <p class="contact-phone">
          <svg width="16" height="16" viewBox="0 0 24 24" fill="var(--navy)" aria-hidden="true"><path d="M6.6 10.8a15 15 0 006.6 6.6l2.2-2.2a1 1 0 011-.25 11.4 11.4 0 003.6.57 1 1 0 011 1V20a1 1 0 01-1 1A17 17 0 013 4a1 1 0 011-1h3.5a1 1 0 011 1c0 1.25.2 2.45.57 3.57a1 1 0 01-.25 1z"/></svg>
          9999-8888
        </p>
      </div>
    </div>
    <div class="brand">
      <div class="brand-row">
        <span class="brand-dot"></span>
        <h1 class="brand-name">Asesorías Nexo Claro</h1>
      </div>
      <p class="brand-tagline">MAPA DE NEGOCIO</p>
    </div>
    <div class="edge-band"></div>
  </section>

  <section class="card card-back" aria-label="Reverso de la tarjeta: lienzo de modelo de negocio">
    <div class="canvas-grid">
      <div class="block partners" title="Socios clave">
        <svg viewBox="0 0 80 80"><rect x="22" y="8" width="24" height="36" rx="12"/><rect x="34" y="36" width="24" height="36" rx="12"/></svg>
      </div>
      <div class="block activities" title="Actividades clave">
        <svg viewBox="0 0 80 80"><path d="M12 14h50a6 6 0 016 6v26a6 6 0 01-6 6H34l-12 12V52H12a6 6 0 01-6-6V20a6 6 0 016-6z"/><path d="M20 28h32M20 38h22"/></svg>
      </div>
      <div class="block resources" title="Recursos clave">
        <svg viewBox="0 0 80 80"><path d="M16 16l48 48M64 16L16 64"/><path d="M8 22l12-12M60 58l12 12"/></svg>
      </div>
      <div class="block value" title="Propuesta de valor">
        <svg viewBox="0 0 80 80"><path d="M40 20a16 16 0 00-9 29v7h18v-7a16 16 0 00-9-29z"/><path d="M32 63h16M40 4v6M14 14l5 5M66 14l-5 5M6 38h6M68 38h6"/></svg>
      </div>
      <div class="block relationships" title="Relación con clientes">
        <svg viewBox="0 0 80 80"><path d="M40 66L14 40a14 14 0 0126-18 14 14 0 0126 18z"/></svg>
      </div>
      <div class="block channels" title="Canales">
        <svg viewBox="0 0 80 80"><rect x="6" y="22" width="42" height="30" rx="3"/><path d="M48 32h14l10 10v10H48z"/><circle cx="20" cy="58" r="6"/><circle cx="60" cy="58" r="6"/></svg>
      </div>
      <div class="block segments" title="Segmentos de clientes">
        <svg viewBox="0 0 80 80"><circle cx="24" cy="30" r="8"/><circle cx="42" cy="28" r="9"/><circle cx="60" cy="30" r="8"/><path d="M10 56c0-8 6-12 14-12M70 56c0-8-6-12-14-12M26 58c0-10 7-14 16-14s16 4 16 14z"/></svg>
      </div>
      <div class="block costs" title="Estructura de costos">
        <svg viewBox="0 0 80 80"><rect x="8" y="14" width="64" height="52" rx="3"/><path d="M22 56V42M34 56V34M46 56V40M58 56V26"/></svg>
      </div>
      <div class="block revenue" title="Fuentes de ingresos">
        <svg viewBox="0 0 80 80"><path d="M30 12h20l-6 12h-8z"/><path d="M36 24C18 34 14 48 16 58a10 10 0 0010 8h28a10 10 0 0010-8c2-10-2-24-20-34"/><path d="M46 40a7 7 0 100 12"/></svg>
      </div>
    </div>
  </section>

</body>
</html>
```